Law Firm from Estonia. E-S-T-O-N-I-A. Country of nice people and bad skiing weather

Just in case there is still a misunderstanding here - this is a project for the Letterhead, Logo and Business Card (i.e THREE designs). Due to some odd reason the system does not always show Logo and Business Card part - we have written an e-mail to the PitchForge support on that.

Our current business name is Vesberg & Lund by two owners.

We want turquoise blue as our corporate colour – against black and white background. As per logo and letterhead design – we would like it to be simple, modern and elegant.

We would like our corporate identity to express the following: best, vanguard, trustworthiness. Our logo must be:
-Classy and precious
-Simple, clean and elegant
-Timeless
-Trustworthy and strong

You should be heading for something LETTERED (we're legal), SIMPLE (we make other people's problems simple), STRAIGHTFORWARD, CORPORATE and CONFIDENT.

1. The Logo shall consist of two main parts: The company name and the symbol.
-The Brand Name is: Vesberg & Lund
-The Symbol must be easy to recognize and clear.
Please suggest 3 symbols.
The name and the symbol must be usable together and separately, in colour (blue-green) and black&white.

Once The Logo has been set, please develop a stationary with the following items:
-Business Card
-Letterhead A4

Suggest 3 of each.

We are looking forward to your designs.
Updates

Dear all, As per light blue colour - could you please use BlueGreen palette (i.e turquoise, aquamarine, cyan blue, sea green etc) - i.e blue should contain a little bit of green. The colour palette provided here does not contain the right tone - the green blue is too green. Our blue should be bluer, but still contain a hint of green. Like, for example, Saharalux products. Thank you!

Dear all, I do not know if you can see your colleagues' designs participating in the same contest, but they look alike as if you are using the same template. Therefore may we suggest that you do not use this horizontal S-wave and do something more creative. Moreover, it's about the LETTER of the law and about being straight - there is nothing in Law that is about waves. Please do NOT use waves! Our logo should be STRAIGHT and SOLID, but ELEGANT. Like Dorval. If you use our initials for logo, you may use different fonts. Just V&L is not appealing, we could create it ourselves in QX Writer. Perhaps putting a full stop at the end of the initials might be interesting. Or, for example, have a look at Orbit Dataworks logo, forming an interesting square from the letters. As per colours - the palette here in PitchForge is very limited and all the colours look dirty. We would like our colours to be bright and clean. May we also suggest that you use colour gradient in some of your designs. We do not insist, but it might make the simple design (that we want) a bit more interesting. Kind regards Marta

Dear all, One of our partners has just suggested the following: The Law Firm's line is like the surgical incision: quick, clean and sharp. We hope it inspires you. Regards Marta

Hello everybody Nobody has ever done it yet, but as a combination of M and K you could use two triangles - if you connect M's legs and turn it clockwise to make it look like K I have unloaded some pictures that just came to my mind. Could you suggest something like this (too) please? Thank you

Dear all, Since your perception of turquoise might be different from ours, please find below a link with the exact colour we want. http://www.hueatlas-example.net/colors/34DDDD OUR LOGO SHOULD BE MONOCHROME - the only colours that are allowed are turquoise (you may use hues), black and white. Please do NOT suggest green & blue, blue & red, red & orange etc. Regards Marta

Reason: One day to the deadline and we are not happy with the results yet. We hope this little extension helps. Regards Marta

Target Market(s)

Our clients are:
- mid- to large-sized companies
- managed by our agemates (let us say 35 and over),
- who are well educated middle-class males, married with children
- western languages speaking (English, Estonian, Scandinavian)

Industry/Entity Type

Business

Font styles to use
Sans Serif
Script

Colors
ecf7f6
ecf7f5
86cfc6
34b8a4
00a98f
33a6d7

Requirements
Should not have
• The design should not use old-style fonts
The design should not use serif fonts
Please do not use inaccurate informal fonts either
Please do not include common stamps of Themis (balance, sword, hammer etc)
Please do not use waves

```html
<!DOCTYPE html>
<html lang="en">
<head>
<meta charset="utf-8">
<title>Vesberg &amp; Lund — Letterhead</title>
<link rel="stylesheet" href="https://fonts.googleapis.com/css2?family=Exo+2:wght@400;500&display=swap">
<style>
  :root {
    --backdrop: #b7dce2;
    --paper: #f1f1f3;
    --ink: #2e3033;
    --ink-soft: #55585c;
    --turquoise: #34b8d4;
    --turquoise-deep: #2a8fbf;
    --signature-tint: #dcdde1;
  }
  * { margin: 0; padding: 0; box-sizing: border-box; }
  html, body { width: 1200px; height: 1000px; overflow: hidden; }
  body {
    background: var(--backdrop);
    font-family: "Exo 2", sans-serif;
    color: var(--ink);
    position: relative;
  }
  .sheet {
    position: absolute;
    background: var(--paper);
  }
  .sheet--first { left: 163px; top: 190px; width: 390px; height: 560px; }
  .sheet--continuation { left: 681px; top: 178px; width: 391px; height: 562px; }

  .brand {
    position: absolute;
    display: flex;
    align-items: center;
    gap: 7px;
  }
  .brand__mark { background: var(--turquoise); flex: none; }
  .brand__name {
    font-weight: 500;
    color: var(--ink);
    text-transform: uppercase;
    line-height: 1;
  }
  .sheet--first .brand { left: 34px; top: 32px; }
  .sheet--first .brand__mark { width: 16px; height: 16px; }
  .sheet--first .brand__name { font-size: 15px; letter-spacing: 0.2px; }
  .sheet--continuation .brand { right: 28px; top: 30px; gap: 4px; }
  .sheet--continuation .brand__mark { width: 8px; height: 8px; }
  .sheet--continuation .brand__name { font-size: 8px; }

  .contact {
    position: absolute;
    left: 277px;
    top: 32px;
    font-size: 3.8px;
    line-height: 6.3px;
    color: var(--ink-soft);
  }
  .contact__firm {
    font-size: 6px;
    line-height: 8px;
    color: var(--turquoise);
    font-weight: 500;
  }
  .contact__label { color: var(--turquoise); }

  .letter {
    position: absolute;
    font-size: 5.6px;
    line-height: 10.3px;
    color: var(--ink-soft);
    text-align: justify;
  }
  .sheet--first .letter { left: 57px; top: 140px; width: 278px; }
  .sheet--continuation .letter { left: 58px; top: 160px; width: 306px; }
  .letter__salutation { margin-bottom: 7px; }
  .letter p + p { margin-top: 20px; }

  .signature {
    position: absolute;
    left: 237px;
    top: 336px;
    width: 92px;
    height: 20px;
    background: var(--signature-tint);
    border-radius: 3px;
  }
</style>
</head>
<body>
  <section class="sheet sheet--first">
    <div class="brand">
      <span class="brand__mark"></span>
      <span class="brand__name">Vesberg<br>&amp; Lund</span>
    </div>
    <address class="contact" style="font-style:normal">
      <div class="contact__firm">Advokaadibüroo Vesberg &amp; Lund</div>
      <div><span class="contact__label">Reg No:</span> 12845930</div>
      <div><span class="contact__label">VAT No:</span> EE108349217</div>
      <div><span class="contact__label">A:</span> Narva mnt 7, 10117 Tallinn, Estonia</div>
      <div><span class="contact__label">T / F:</span> +372 600 1180 / +372 600 1181</div>
      <div><span class="contact__label">W:</span> info@vesberglund.ee / www.vesberglund.ee</div>
    </address>
    <div class="letter">
      <div class="letter__salutation">Dear Client</div>
      <p>Lorem ipsum dolor sit amet, consectetur adipiscing elit. Nulla sodales nisi vitae Lorem ipsum dolor sit amet, consectetur adipiscing elit. Suspendisse feugiat eros nisl, a facilisis risus eleifend sed. Aliquam mauris enim, fermentum eu lacinia sit amet, laoreet eu leo. Nullam eleifend nulla in libero tristique, ac vulputate odio tincidunt. Etiam non condimentum tortor. Integer suscipit neque nec odio porttitor cursus. Phasellus a sapien blandit, suscipit justo id, condimentum ante. Morbi tristique justo risus, id mattis dui molestie ut. Nullam volutpat ut quam commodo faucibus. Pellentesque urna est, interdum in elit quis, pharetra elementum orci. Nam pharetra velit molestie justo placerat scelerisque.</p>
      <p>Nullam aliquam ligula ac sem aliquet varius. Nullam sed laoreet sapien. Fusce ultricies lobortis odio, sed imperdiet magna lacinia egestas. Morbi vitae varius nibh. Phasellus purus felis, congue id tempor quis, porttitor ut sem. Integer turpis nunc, posuere at quam interdum, interdum pharetra lectus. Fusce commodo sapien vel consequat tincidunt. Proin sed nisl dignissim, accumsan dui ut, luctus turpis. Praesent vulputate elementum nibh. Ut volutpat felis ut mi tincidunt, vitae accumsan quam porta. Sed malesuada bibendum lectus tempor ullamcorper. Nullam interdum diam velit, id porta elit congue quis.</p>
      <p>Pellentesque habitant morbi tristique senectus et netus et malesuada fames ac turpis egestas. Donec quis fermentum massa. Vivamus auctor tincidunt tellus, vel iaculis elit sagittis sit amet. Morbi aliquam pharetra lobortis. Mauris non iaculis ipsum. Morbi tortor ipsum, suscipit a laoreet sed, tempus non risus. Maecenas rhoncus vehicula est, sagittis vulputate magna ullamcorper non. Sed dignissim sapien sed rhoncus imperdiet.</p>
      <p>Proin sed nisl dignissim, accumsan dui ut, luctus turpis. Praesent vulputate elementum nibh. Ut volutpat felis ut mi tincidunt, vitae accumsan quam porta. Sed malesuada bibendum lectus tempor ullamcorper. Nullam interdum diam velit, id porta elit congue quis.</p>
    </div>
  </section>

  <section class="sheet sheet--continuation">
    <div class="brand">
      <span class="brand__mark"></span>
      <span class="brand__name">Vesberg<br>&amp; Lund</span>
    </div>
    <div class="letter">
      <p>Nullam aliquam ligula ac sem aliquet varius. Nullam sed laoreet sapien. Fusce ultricies lobortis odio, sed imperdiet magna lacinia egestas. Morbi vitae varius nibh. Phasellus purus felis, congue id tempor quis, porttitor ut sem. Integer turpis nunc, posuere at quam interdum, interdum pharetra lectus. Fusce commodo sapien vel consequat tincidunt. Proin sed nisl dignissim, accumsan dui ut, luctus turpis. Praesent vulputate elementum nibh. Ut volutpat felis ut mi tincidunt, vitae accumsan quam porta. Sed malesuada bibendum lectus tempor ullamcorper. Nullam interdum diam velit, id porta elit congue quis.</p>
      <p>Pellentesque habitant morbi tristique senectus et netus et malesuada fames ac turpis egestas. Donec quis fermentum massa. Vivamus auctor tincidunt tellus, vel iaculis elit sagittis sit amet. Morbi aliquam pharetra lobortis. Mauris non iaculis ipsum. Morbi tortor ipsum, suscipit a laoreet sed, tempus non risus. Maecenas rhoncus vehicula est, sagittis vulputate magna ullamcorper non. Sed dignissim sapien sed rhoncus imperdiet.</p>
    </div>
    <div class="signature" role="img" aria-label="Handwritten signature of Karl Tamm"></div>
  </section>
</body>
</html>
```